Sophisticated, clean website reflecting my feminine, playful side to sell my abstract art,

I need a website no more than 3 pages to showcase my paintings, a little about me and some contact info. I do abstracts so looking for something a little edgy, yet feminine and current.
Updates

Hi there, These are some artists websites that I Iike: Mirabelvoss.com (I like how airy it is) tobiasmerrowind.com kevinplodderas.com (I like how it scrolls) I'll need a place for a photo ( a headshot-i do not have it yet so I'll need to be able to upload that later) as well as an area for my bio. Also, it's important that I will be able to upload any new photos and descriptions easily so it should be user friendly. Lastly, I like in a sunny place so would like to have this seem upbeat and playful as that is how i like to paint. thanks-I'm trying to upload my photos now -

Target Market(s)

ppl ages 35-70 who want large scale art for their homes

Industry/Entity Type

art

Coding

Coded - Design and coding required

Number of Pages Required

3 page

Colors

Designer to choose colors to be used in the design.

Requirements
Must have
• photos of my art, a place for my bio, be easy to reach me. tasteful-nothing too "in your face" -my clients are pretty high end and organized. They like clean lines
Nice to have
• sophisticated background, muted tones in the back-similar clean font throughout-no cursive
Should not have
• too many dark areas. Too many blocks of color. Too serious.

```html
<!DOCTYPE html>
<html lang="en">
<head>
<meta charset="utf-8">
<title>About Marisol Hartwell</title>
<link rel="stylesheet" href="https://fonts.googleapis.com/css2?family=Oswald:wght@300;400&family=Open+Sans:wght@400&display=swap">
<style>
  :root {
    --ink: #1b1c1a;
    --paper: #ffffff;
    --gold: #9c8a58;
    --gold-line: #c8bf9c;
    --mark-fill: #1a1c1a;
    --mark-frame: #b8aa7e;
    --photo-warm: #b8875a;
    --photo-light: #ece8df;
  }
  * { margin: 0; padding: 0; box-sizing: border-box; }
  html, body { width: 1200px; height: 1012px; overflow: hidden; background: var(--paper); }
  body { position: relative; color: var(--ink); font-family: "Open Sans", sans-serif; }

  .brand-mark {
    position: absolute; left: 514px; top: 40px; width: 164px; height: 165px;
    background: var(--mark-fill); border: 4px solid var(--mark-frame);
  }
  .brand-name {
    position: absolute; left: 0; width: 1200px; top: 218px; text-align: center;
    font-family: "Oswald", sans-serif; font-weight: 300; font-size: 32px; letter-spacing: 0.4px;
  }

  .rule {
    position: absolute; left: 48px; width: 1111px; height: 2px;
    background: linear-gradient(90deg, transparent, var(--gold-line) 18%, var(--gold-line) 82%, transparent);
  }
  .rule--nav-top { top: 276px; }
  .rule--nav-bottom { top: 331px; }
  .rule--foot-top { top: 925px; }
  .rule--foot-bottom { top: 979px; }

  .main-nav {
    position: absolute; left: 0; width: 1200px; top: 291px; display: flex; justify-content: center; gap: 58px;
    font-family: "Oswald", sans-serif; font-weight: 300; font-size: 19px; letter-spacing: 0.4px;
  }
  .main-nav a { color: var(--ink); text-decoration: none; }
  .main-nav a.is-current { color: var(--gold); }

  .bio { position: absolute; left: 121px; top: 388px; width: 600px; }
  .bio h1 {
    font-family: "Oswald", sans-serif; font-weight: 300; font-size: 46px; line-height: 60px; letter-spacing: 0.2px;
    margin-bottom: 10px;
  }
  .bio p { font-size: 16.5px; line-height: 31.6px; margin-bottom: 31.6px; letter-spacing: 0.45px; }
  .bio p span { display: block; white-space: nowrap; }

  .portrait {
    position: absolute; left: 737px; top: 389px; width: 370px; height: 413px;
    background: linear-gradient(160deg, var(--photo-light) 0%, #d9b58e 30%, var(--photo-warm) 60%, #9a6c45 100%);
    clip-path: polygon(14% 6%, 30% 0%, 55% 10%, 78% 16%, 100% 30%, 93% 70%, 75% 92%, 58% 100%, 35% 96%, 2% 95%, 0% 60%, 8% 45%, 10% 20%);
  }

  .social { position: absolute; left: 521px; top: 887px; display: flex; gap: 42px; }
  .social span { width: 16px; height: 16px; border-radius: 50%; background: var(--ink); display: block; }

  .copyright {
    position: absolute; left: 0; width: 1200px; top: 941px; text-align: center;
    font-family: "Oswald", sans-serif; font-weight: 300; font-size: 17px;
  }
</style>
</head>
<body>
  <header>
    <div class="brand-mark" aria-hidden="true"></div>
    <div class="brand-name">Marisol Hartwell</div>
    <div class="rule rule--nav-top"></div>
    <nav class="main-nav">
      <a href="#">HOME</a>
      <a href="#" class="is-current">ABOUT ME</a>
      <a href="#">CONTACT</a>
    </nav>
    <div class="rule rule--nav-bottom"></div>
  </header>

  <main>
    <section class="bio">
      <h1>About Marisol Hartwell</h1>
      <p>
        <span>Lorem Ipsum is simply dummy text of the printing and typesetting</span>
        <span>industry. Lorem Ipsum has been the industry's standard dummy</span>
        <span>text ever since the 1500s, when an unknown printer took a galley</span>
        <span>of type and scrambled it to make a type specimen book.</span>
      </p>
      <p>
        <span>It has survived not only five centuries, but also the leap into</span>
        <span>electronic typesetting, remaining essentially unchanged. It was</span>
        <span>popularised in the 1960s with the release of Linotrace sheets</span>
        <span>containing Lorem Ipsum passages, and more recently with</span>
        <span>desktop publishing software like Orvell PageCraft including</span>
        <span>versions of Lorem Ipsum.</span>
      </p>
    </section>
    <div class="portrait" role="img" aria-label="Portrait of the artist holding a paintbrush, framed in a brush-stroke shape"></div>
  </main>

  <footer>
    <div class="social" aria-label="Social links">
      <span role="img" aria-label="Social profile one"></span>
      <span role="img" aria-label="Social profile two"></span>
      <span role="img" aria-label="Social profile three"></span>
    </div>
    <div class="rule rule--foot-top"></div>
    <div class="copyright">Copyright 2022, Marisol Hartwell</div>
    <div class="rule rule--foot-bottom"></div>
  </footer>
</body>
</html>
```